Business Card & Logo Design - Hedge Fund

We need a business card and logo design for a hedge fund. The hedge fund is named Morvane Equity LLC. Morvane Equity was created by finance professors and the strategy is based academic research that looks for patterns in stock prices. The design should look conservative, solid, strong. We favor a classic style - nothing flashy. The logo can relate to the name Morvane Equity, or it could involve a symbol design that connotes "science" . We are open to ideas. We do not want alot of colors - but if any, color - blue is preferred. The font that seems to look best for the name (Morvane Equity) is arial black. We are open to ideas. Most important - we want to see a mock up of an actual business card with the logo concept embedded. The business card should include space for : company name, individual name, position title, cell phone, address. We hope to have this work done by Sept. 8.

Target Market(s)

We will be meeting with and giving the business card to institutions and high net worth individuals.

Industry/Entity Type

Investment Advisory

Contact Information for Business Card

Company name - Morvane Equity LLC
Individual name - Peter Dalby
Title - Portfolio Manager
Cell - (412) 555-0187
Address - 2650 Birchmont Lane, Suite 300, Atlanta GA 30327

Font styles to use
Other font styles liked:
• Arial

Colors
3277b5
0255a3
85acd3
cedeed
fdf9cf
d9d9d9
e6e6e6
f04a50
6b449b

Requirements
Must have
• Must have card details that are sited above.
• We would like a logo related to the name (Morvane Equity) or concept of the fund.
Nice to have
• We want conservative / understated / clean crisp look.
• If any colors - we prefer conservative appearance - blue / gray.
• I have enclosed an example of a card style that looks attractive - please do not exactly copy this card. This is not our company or logo. I feel the layout is attractive - just as an example
Should not have
• Avoid too much color.
• I have selected some preferred colors. Please do not use all of the colors - I have selected a few that might work - but I am not sure. We are open to your ideas so please do not feel the need to use all or any of these.

```html
<!DOCTYPE html>
<html lang="en">
<head>
<meta charset="utf-8">
<title>Morvane Equity LLC – Logo &amp; Business Card</title>
<link rel="stylesheet" href="https://fonts.googleapis.com/css2?family=Arimo:wght@400;700&display=swap">
<style>
  :root {
    --brand-blue: #0255a3;
    --card-blue: #3277b5;
    --stone-gray: #d9d9d9;
    --ink: #1d1d1b;
    --paper: #ffffff;
  }
  html, body {
    margin: 0;
    padding: 0;
    overflow: hidden;
  }
  body {
    width: 1200px;
    height: 1200px;
    background: var(--paper);
    font-family: "Arimo", Arial, sans-serif;
    position: relative;
  }
  .brand-block {
    position: absolute;
    left: 0;
    top: 0;
    width: 1200px;
    height: 470px;
  }
  .brand-square {
    position: absolute;
    left: 570px;
    top: 250px;
    width: 120px;
    height: 120px;
    background: var(--brand-blue);
  }
  .brand-name {
    position: absolute;
    left: 0;
    width: 1268px;
    top: 400px;
    margin: 0;
    text-align: center;
    font-weight: 700;
    font-size: 44px;
    letter-spacing: 0.5px;
    color: var(--ink);
  }
  .business-card {
    position: absolute;
    left: 437px;
    top: 508px;
    width: 337px;
    height: 589px;
  }
  .card-front {
    height: 324px;
    background: var(--stone-gray);
    position: relative;
  }
  .card-square {
    position: absolute;
    left: 138px;
    top: 150px;
    width: 56px;
    height: 56px;
    background: var(--brand-blue);
  }
  .card-brand {
    position: absolute;
    left: 0;
    right: -10px;
    top: 232px;
    margin: 0;
    text-align: center;
    font-weight: 700;
    font-size: 16px;
    color: var(--paper);
  }
  .card-contact {
    height: 265px;
    background: var(--card-blue);
    color: var(--paper);
    text-align: center;
    box-sizing: border-box;
    padding-top: 59px;
  }
  .contact-name {
    margin: 0 0 4px;
    font-weight: 700;
    font-size: 22px;
    line-height: 26px;
  }
  .contact-line {
    margin: 0;
    font-size: 14px;
    line-height: 23.3px;
  }
</style>
</head>
<body>
  <header class="brand-block">
    <div class="brand-square" aria-hidden="true"></div>
    <h1 class="brand-name">MORVANE EQUITY LLC</h1>
  </header>

  <section class="business-card" aria-label="Business card">
    <div class="card-front">
      <div class="card-square" aria-hidden="true"></div>
      <p class="card-brand">MORVANE EQUITY LLC</p>
    </div>
    <div class="card-contact">
      <p class="contact-name">Peter Dalby</p>
      <p class="contact-line">Morvane Equity LLC</p>
      <p class="contact-line">Portfolio Manager</p>
      <p class="contact-line">M- (412) 555-0187</p>
      <p class="contact-line">2650 Birchmont Lane, Suite 300, Atlanta</p>
      <p class="contact-line">GA 30327</p>
    </div>
  </section>
</body>
</html>
```